Velmora and Co Business Card Design

Looking for a business card design. Wanting Smart, Clean and Sharp looking to promote Velmora and Co, our Import Export Business - like Black, White and natural textures. I have uploaded our logo. I like a rounded font but open to other ideas
Being that we have a wide range of products on offer we are looking for a neutral yet eye catching card. We would also like to have Import - Export on the business card to be clear on want our business does.

Target Market(s)

Import export market

Industry/Entity Type

Importer

Contact Information for Business Card

Mr Tobias Kernwell
tobias.kernwell@velmoraandco.com.au
+61 (0) 417 630 284
www.velmoraandco.com.au

Font styles to use
Other font styles liked:
• Unsure of actual font name but something rounded and clean

Colors

Designer to choose colors to be used in the design.

Requirements
Must have
• Instagram icon
• Facebook icon

```html
<!DOCTYPE html>
<html lang="en">
<head>
<meta charset="utf-8">
<title>Velmora and Co Business Card</title>
<link rel="stylesheet" href="https://fonts.googleapis.com/css2?family=Oswald:wght@500&family=Arimo:wght@400;700&display=swap">
<style>
  :root {
    --page-bg: #e6e6e4;
    --card-white: #ffffff;
    --card-black: #1f1d1d;
    --ink-black: #1c1a1a;
    --ink-white: #ffffff;
    --ink-soft: #d9d9d9;
    --divider: #8a8a8a;
  }
  * { box-sizing: border-box; margin: 0; padding: 0; }
  html, body {
    width: 1200px;
    height: 800px;
    overflow: hidden;
    background: var(--page-bg);
  }
  .canvas {
    width: 1200px;
    height: 800px;
    display: flex;
    align-items: center;
    justify-content: center;
    gap: 40px;
  }
  .card {
    width: 540px;
    height: 309px;
    position: relative;
    box-shadow: 0 10px 30px rgba(0,0,0,0.18);
  }
  .card--front {
    background: var(--card-white);
    display: flex;
    flex-direction: column;
    align-items: center;
    justify-content: center;
    gap: 10px;
  }
  .brand {
    display: flex;
    align-items: center;
    gap: 12px;
  }
  .brand__mark {
    width: 22px;
    height: 22px;
    background: var(--ink-black);
  }
  .brand__name {
    font-family: "Oswald", sans-serif;
    font-weight: 500;
    font-size: 38px;
    letter-spacing: 1px;
    line-height: 1;
    color: var(--ink-black);
    text-transform: uppercase;
  }
  .brand__tagline {
    font-family: "Arimo", sans-serif;
    font-size: 11px;
    letter-spacing: 4px;
    color: var(--ink-black);
    text-transform: uppercase;
    padding-left: 34px;
  }
  .card--back {
    background: var(--card-black);
    display: flex;
    align-items: center;
    padding-left: 42px;
  }
  .holder-name {
    font-family: "Oswald", sans-serif;
    font-weight: 500;
    font-size: 21px;
    color: var(--ink-white);
    text-transform: uppercase;
    letter-spacing: 0.2px;
    white-space: nowrap;
  }
  .divider {
    width: 1px;
    height: 80px;
    background: var(--divider);
    margin: 0 14px;
  }
  .contacts {
    list-style: none;
    font-family: "Arimo", sans-serif;
    font-size: 12px;
    line-height: 19px;
    color: var(--ink-soft);
  }
  .contacts li {
    display: flex;
    align-items: center;
    gap: 7px;
    white-space: nowrap;
  }
  .contacts svg {
    width: 10px;
    height: 10px;
    flex: none;
  }
  .contacts strong { font-weight: 700; color: var(--ink-white); }
  .social-dots { display: flex; gap: 3px; }
  .social-dot {
    width: 10px;
    height: 10px;
    border-radius: 50%;
    background: var(--ink-white);
  }
</style>
</head>
<body>
  <main class="canvas">
    <section class="card card--front" aria-label="Card front">
      <div class="brand">
        <span class="brand__mark"></span>
        <span class="brand__name">Velmora &amp; Co</span>
      </div>
      <p class="brand__tagline">Import &ndash; Export</p>
    </section>

    <section class="card card--back" aria-label="Card back">
      <p class="holder-name">Mr Tobias Kernwell</p>
      <span class="divider"></span>
      <ul class="contacts">
        <li>
          <svg viewBox="0 0 10 10" aria-hidden="true"><rect x="2" y="0.8" width="6" height="8.4" rx="1" fill="none" stroke="#ffffff" stroke-width="1.2"/></svg>
          <span>+61 (0) 417 630 284</span>
        </li>
        <li>
          <svg viewBox="0 0 10 10" aria-hidden="true"><rect x="0.6" y="1.8" width="8.8" height="6.4" fill="#ffffff"/><path d="M0.6 1.8 L5 5.6 L9.4 1.8" fill="none" stroke="#1f1d1d" stroke-width="1"/></svg>
          <span>tobias.kernwell@velmoraandco.com.au</span>
        </li>
        <li>
          <svg viewBox="0 0 10 10" aria-hidden="true"><circle cx="5" cy="5" r="4.4" fill="#ffffff"/><path d="M0.6 5 H9.4 M5 0.6 C3 3 3 7 5 9.4 M5 0.6 C7 3 7 7 5 9.4" fill="none" stroke="#1f1d1d" stroke-width="0.7"/></svg>
          <span>www.<strong>velmoraandco</strong>.com.au</span>
        </li>
        <li>
          <span class="social-dots" aria-hidden="true"><span class="social-dot"></span><span class="social-dot"></span></span>
          <span>/velmoraandco</span>
        </li>
      </ul>
    </section>
  </main>
</body>
</html>
```